Amazing new protein bar on the market - be a part of something special

We need packaging design for the wrapper for great tasting new protein. The product is called "Copperleaf Crisp". The packaging should have a modern font and design I catching - Copperleaf Crisp. If possible we would like to incorporate a picture of the bar in the background. The font and name of the bar should stand out and jump out at you. Modern font is a must. The product run will be blueberry - pomegranate. Please use bright colors, White, Red and/or Orange. Lightning bolts would be a plus.
Updates

Project Deadline Extended Reason: We have changed our product name. Would like to see more designs. Added Monday, April 17, 2017

Target Market(s)

Athletes, people on the go or on a diet

Industry/Entity Type

Product

Logo Text

Copperleaf Crisp

Colors
f04a51
f68e4e
faa54b
ffffff

Requirements
Must have
• Prefer modern font that jumps out at you. Slanted if possible
• Please use bright colors White, Red and/or Orange

```html
<!DOCTYPE html>
<html lang="en">
<head>
<meta charset="utf-8">
<title>Copperleaf Crisp – Wrapper</title>
<link rel="stylesheet" href="https://fonts.googleapis.com/css2?family=Montserrat:ital,wght@0,300;0,400;0,600;1,900&display=swap">
<style>
  :root {
    --page: #fbe9cf;
    --red: #e31e24;
    --red-deep: #c4161c;
    --red-crimp: #d81c22;
    --yellow: #ffe93a;
    --orange: #f68e4e;
    --amber: #faa54b;
    --white: #ffffff;
  }
  * { margin: 0; padding: 0; box-sizing: border-box; }
  html, body { width: 1200px; height: 657px; overflow: hidden; }
  body { background: var(--page); font-family: "Montserrat", sans-serif; position: relative; }

  .wrapper { position: absolute; left: 76px; top: 188px; width: 1068px; height: 356px; }
  .wrapper-shape { position: absolute; inset: 0; width: 100%; height: 100%; }

  .product-shot {
    position: absolute; left: 300px; top: 124px; width: 352px; height: 136px; border-radius: 44px;
    background: radial-gradient(ellipse at 50% 50%, #d99a5f 0%, #c97b45 45%, #b7424f 75%, rgba(183,66,79,0) 100%);
  }

  .product-name {
    position: absolute; left: 368px; top: 38px; width: 420px;
    font-weight: 900; font-style: italic; color: var(--red); line-height: 1; letter-spacing: -1px;
    font-size: 70px;
  }
  .product-name .line-one { display: block; }
  .product-name .line-two { display: block; text-align: right; }

  .weight { position: absolute; left: 140px; top: 266px; color: var(--white); }
  .weight .grams { font-size: 24px; font-weight: 300; }
  .weight .grams small { font-size: 12px; font-weight: 400; }
  .weight .net { display: block; font-size: 11.5px; font-weight: 600; margin-top: 6px; }

  .flavour {
    position: absolute; left: 769px; top: 268px; width: 240px;
    color: var(--white); font-size: 12px; line-height: 1.4; font-weight: 400;
  }
  .flavour strong { font-weight: 600; }
</style>
</head>
<body>
  <div class="wrapper">
    <svg class="wrapper-shape" viewBox="0 0 1068 356" aria-hidden="true">
      <defs>
        <linearGradient id="body-red" x1="0" y1="0" x2="0" y2="1">
          <stop offset="0" stop-color="#ea2a2f"/>
          <stop offset="0.6" stop-color="#e31e24"/>
          <stop offset="1" stop-color="#c4161c"/>
        </linearGradient>
        <radialGradient id="panel-glow" cx="0.55" cy="0.25" r="0.8">
          <stop offset="0" stop-color="#fff9b0"/>
          <stop offset="0.4" stop-color="#ffe93a"/>
          <stop offset="1" stop-color="#faa54b"/>
        </radialGradient>
        <linearGradient id="silver" x1="0" y1="0" x2="1" y2="0">
          <stop offset="0" stop-color="#cfcfcf"/>
          <stop offset="0.4" stop-color="#f2f2f2"/>
          <stop offset="0.7" stop-color="#8a8a8a"/>
          <stop offset="1" stop-color="#e0e0e0"/>
        </linearGradient>
        <pattern id="crimp-lines" width="5" height="10" patternUnits="userSpaceOnUse">
          <rect width="5" height="10" fill="#d81c22"/>
          <rect width="1.5" height="10" fill="#b8141a"/>
        </pattern>
      </defs>
      <rect class="crimp-left" x="0" y="0" width="62" height="356" fill="url(#crimp-lines)"/>
      <rect class="crimp-right" x="1006" y="0" width="62" height="356" fill="url(#crimp-lines)"/>
      <rect class="body" x="50" y="26" width="968" height="306" fill="url(#body-red)"/>
      <path class="panel" d="M330,26 C262,96 232,240 330,302 C470,362 760,300 996,26 Z" fill="url(#panel-glow)"/>
      <path class="swoosh" d="M330,26 C262,96 232,240 330,302 C470,362 760,300 996,26" fill="none" stroke="url(#silver)" stroke-width="10"/>
      <circle class="badge" cx="192" cy="104" r="60" fill="#ffe93a" stroke="#faa54b" stroke-width="3"/>
    </svg>

    <div class="product-shot" role="img" aria-label="Photo of the blueberry pomegranate crisp bar with white drizzle, blueberries and pomegranate seeds"></div>

    <h1 class="product-name"><span class="line-one">Copperleaf</span><span class="line-two">Crisp</span></h1>

    <div class="weight">
      <span class="grams">28g <small>bars</small></span>
      <span class="net">NET WT. 0.99 oz</span>
    </div>

    <p class="flavour">Naturally and artificially<br>flavoured <strong>BLUEBERRY</strong><br>POMEGRANATE crisp protein bar</p>
  </div>
</body>
</html>
```